We need a podcast cover design that will be used on Vexora. The podcast is called Founder Temperament Dial. The people we want to attract want us to be direct, real and upfront wiht them. They live in a noisy world and want clear and elegant design and funciton. We work with entrepreneurs who like brands like Quorla, Zentrix and Movari. We want a simple elegant design that uses the title on the cover along with the photo we uploaded. If someone goes to vexora, we want this to stand out and be visible.

Target Market(s)

Entrepreneurs, Artists, People who think differently

Industry/Entity Type

Consultant

Font styles to use
Sans Serif

Colors

Designer to choose colors to be used in the design.

Requirements
Must have
• The title on the podcast cover that will be legible on vExora. There should be high contrast so that the cover stands out on vexora with everyoe else.
Nice to have
• I would like to see the photo offset either right or left and bleeding off the page.
Should not have
• Too many colors, patterns or designs. Simple, elegant, and clean.

```html
<!DOCTYPE html>
<html lang="en">
<head>
<meta charset="UTF-8">
<title>Founder Temperament Dial — Podcast Cover</title>
<link rel="stylesheet" href="https://fonts.googleapis.com/css2?family=Raleway:wght@200;300;800&display=swap">
<style>
  :root {
    --bg-deep: #0b1c21;
    --bg-glow: #1f5a63;
    --bar-light: #d8eef2;
    --bar-fade: rgba(140, 190, 200, 0.35);
    --title-dark: #163a42;
    --title-white: #ffffff;
    --title-fade: rgba(190, 205, 210, 0.25);
    --photo-skin: #c58d6a;
    --photo-shirt: #8fd3ea;
  }
  * { margin: 0; padding: 0; box-sizing: border-box; }
  html, body {
    width: 1200px;
    height: 1200px;
    overflow: hidden;
    background: var(--bg-deep);
  }
  .cover {
    position: relative;
    width: 1200px;
    height: 1200px;
    overflow: hidden;
    background: radial-gradient(ellipse 60% 55% at 60% 55%, var(--bg-glow) 0%, #143a42 45%, var(--bg-deep) 100%);
    font-family: 'Raleway', sans-serif;
  }
  .host-photo {
    position: absolute;
    left: 0;
    top: 0;
    width: 1200px;
    height: 1200px;
  }
  .title-bar {
    position: absolute;
    left: 540px;
    top: 322px;
    width: 660px;
    height: 80px;
    background: linear-gradient(90deg, var(--bar-fade) 0%, var(--bar-light) 20%, var(--bar-light) 80%, var(--bar-fade) 100%);
    box-shadow: 0 0 40px rgba(200, 235, 240, 0.35);
  }
  .title-kicker {
    position: absolute;
    left: 590px;
    top: 332px;
    font-weight: 800;
    font-size: 52px;
    line-height: 60px;
    letter-spacing: 1px;
    color: var(--title-dark);
  }
  .title-middle {
    position: absolute;
    left: 552px;
    top: 455px;
    font-weight: 300;
    font-size: 84px;
    line-height: 90px;
    letter-spacing: 1px;
    color: var(--title-white);
  }
  .title-main {
    position: absolute;
    left: 548px;
    top: 535px;
    font-weight: 200;
    font-size: 250px;
    line-height: 250px;
    letter-spacing: 8px;
    background: linear-gradient(180deg, var(--title-white) 35%, var(--title-fade) 100%);
    -webkit-background-clip: text;
    background-clip: text;
    color: transparent;
  }
</style>
</head>
<body>
  <main class="cover">
    <svg class="host-photo" viewBox="0 0 1200 1200" role="img" aria-label="Photo of the smiling host in a light blue athletic shirt, offset left and bleeding off the bottom">
      <defs>
        <linearGradient id="hostTone" x1="0" y1="0" x2="0" y2="1">
          <stop offset="0" stop-color="#2a1e18"/>
          <stop offset="0.12" stop-color="var(--photo-skin)"/>
          <stop offset="0.55" stop-color="#a8704f"/>
          <stop offset="0.66" stop-color="var(--photo-shirt)"/>
          <stop offset="1" stop-color="#7cc3dc"/>
        </linearGradient>
      </defs>
      <path fill="url(#hostTone)" d="M0,860 C60,830 140,790 200,730 C150,650 70,560 40,420 C30,300 50,180 100,110 C170,40 300,30 420,60 C500,90 540,190 530,330 C525,430 500,560 440,670 C470,720 560,760 700,790 C860,830 980,900 1030,1000 C1050,1080 1050,1150 1044,1200 L0,1200 Z"/>
    </svg>

    <div class="title-bar"></div>
    <h1 class="podcast-title">
      <span class="title-kicker">FOUNDER</span>
      <span class="title-middle">TEMPERAMENT</span>
      <span class="title-main">DIAL</span>
    </h1>
  </main>
</body>
</html>
```